K5Lesson WebSite

an educational website about tutoring, client will be surfing this site looking for a tutor, please see the attached images because the contains exactly what we need.
Updates

Project Deadline Extended Reason: something went wrong with the uploaded files, we are very sorry.thank you PixelBazaar for the 5 days extension.now there is a 3 images describing the content of the three pages.good luck Added Friday, August 5, 2016

Target Market(s)

everyone

Industry/Entity Type

Education

Number of Pages Required

3 page

Font styles to use
Other font styles liked:
• something looks good in Arabic and english like "Droid Arabic Kufi"

Requirements
Must have
• the logo we attached, responsive design, simple, also try as much as you can Centering texts and layout because this website will have an Arabic version, Arabic is a Right-to-Left Language.
• a change language button,
Nice to have
• educational gestures.
• Centered texts and layout because this website will have an Arabic version, Arabic is a Right-to-Left Language.
• we have a web designer and we can download any template and add our logo and text to it, but.....
• we need creativity, so please stick to the contents in the images we attached, we need something very simple, more like a varnel home page with little touch of filtering fields like the 5 dropdownlist and the gender selection buttons.
• try not to go far away from the contents we specified in the images, use less images or dont use images at all, try not to make the client scroll down,
Should not have
• too much colors or noisy layout or heavy media

```html
<!DOCTYPE html>
<html lang="en">
<head>
<meta charset="utf-8">
<title>K5Lesson – Online Tutoring</title>
<link href="https://fonts.googleapis.com/css2?family=Oswald:wght@500&family=Roboto:wght@400;500;700&display=swap" rel="stylesheet">
<style>
:root{
  --blue:#1a72c0;
  --blue-dark:#125fa3;
  --orange:#f26522;
  --green:#8cc63f;
  --sky:#29abe2;
  --ink:#222;
  --muted:#666;
  --band:#eef0f2;
  --dark:#2a2d33;
  --black:#141414;
  --white:#fff;
}
*{box-sizing:border-box;margin:0;padding:0}
html,body{width:1200px;height:2795px;overflow:hidden}
body{position:relative;font-family:"Roboto",Arial,sans-serif;color:var(--ink);background:var(--white)}
section,header,footer,nav,div{position:absolute}
.topbar{left:0;top:0;width:1200px;height:46px;background:var(--blue);color:var(--white);font-size:14px;z-index:2}
.topbar .contact{left:90px;top:14px;display:flex;gap:30px}
.topbar .contact span{display:flex;align-items:center;gap:8px;position:static}
.topbar .lang{left:855px;top:14px;font-size:13px}
.topbar .social{left:970px;top:12px;display:flex;gap:10px}
.topbar .social i{display:block;width:20px;height:20px;border-radius:3px;background:rgba(255,255,255,.85)}
.nav{left:0;top:46px;width:1200px;height:98px;background:var(--white)}
.logo{left:90px;top:26px;display:flex;align-items:center;gap:10px;font-size:36px;font-weight:700;color:var(--blue);line-height:44px}
.logo i{display:block;width:38px;height:38px;background:var(--orange)}
.menu{left:470px;top:38px;display:flex;gap:28px;font-size:15px;color:#444;white-space:nowrap}
.menu a{color:inherit;text-decoration:none}
.menu .active{color:var(--orange)}
.hero{left:0;top:144px;width:1200px;height:588px;background:linear-gradient(100deg,#c7a88c 0%,#e8d9c6 35%,#d5c0a6 60%,#a98a6a 100%)}
.hero h1{left:90px;top:428px;font-family:"Oswald",sans-serif;font-weight:500;font-size:50px;color:var(--white);text-shadow:0 2px 6px rgba(0,0,0,.4);white-space:nowrap;position:absolute}
.hero p{left:96px;top:490px;font-family:"Oswald",sans-serif;font-size:27px;color:var(--white);text-shadow:0 2px 6px rgba(0,0,0,.4);position:absolute;white-space:nowrap}
.hero .arrow{top:474px;width:38px;height:38px;border-radius:50%;background:rgba(0,0,0,.55)}
.welcome{left:0;top:732px;width:1200px;height:213px;text-align:center}
h2{font-size:26px;font-weight:500;color:var(--ink)}
h2 b{font-weight:500;color:var(--blue)}
.welcome h2{position:absolute;left:0;top:42px;width:1200px}
.welcome p{position:absolute;left:90px;top:90px;width:1020px;font-size:13px;line-height:25px;color:var(--muted)}
.steps{left:0;top:945px;width:1200px;height:315px;background:var(--band)}
.step{top:56px;width:300px;text-align:center}
.step .dot{position:relative;margin:0 auto;width:108px;height:108px;border-radius:50%;border:5px solid #fff;box-shadow:0 2px 6px rgba(0,0,0,.15);display:flex;align-items:center;justify-content:center}
.step h3{margin-top:28px;font-size:20px;font-weight:500}
.step p{margin-top:12px;font-size:13px;color:var(--muted);line-height:20px}
.about{left:0;top:1260px;width:1200px;height:408px}
.about .photo{left:90px;top:80px;width:441px;height:264px;border:6px solid #fff;box-shadow:0 1px 6px rgba(0,0,0,.3);background:linear-gradient(120deg,#c9d7e3,#e6ddd2 55%,#a9b9c8)}
.about h2{position:absolute;left:561px;top:76px}
.about p{position:absolute;left:564px;width:546px;font-size:13px;line-height:24px;color:var(--muted)}
.btn-green{left:564px;top:305px;width:120px;height:39px;background:var(--green);color:#fff;font-size:15px;font-weight:500;display:flex;align-items:center;justify-content:center}
.courses{left:0;top:1668px;width:1200px;height:313px;background:linear-gradient(90deg,#3b3e44,var(--dark) 50%,#46494f);text-align:center;color:#fff}
.courses h2{position:absolute;left:0;top:70px;width:1200px;color:#fff;font-size:32px}
.courses p{position:absolute;left:110px;top:120px;width:980px;font-size:16px;font-weight:500;line-height:32px}
.btn-ghost{left:533px;top:208px;width:134px;height:45px;border:1px solid #fff;border-radius:6px;font-size:15px;display:flex;align-items:center;justify-content:center}
.tutors{left:0;top:1981px;width:1200px;height:471px}
.tutors h2{position:absolute;left:0;top:70px;width:1200px;text-align:center}
.tutor{top:145px;width:220px;text-align:center}
.tutor .face{position:relative;margin:0 auto;width:126px;height:126px;border-radius:50%;border:5px solid #fff;box-shadow:0 0 0 1px #ccc,0 2px 5px rgba(0,0,0,.2);background:linear-gradient(160deg,#d9d9d9,#a8a8a8)}
.tutor h4{margin-top:24px;font-size:15px;font-weight:500}
.tutor p{margin-top:8px;font-size:11px;line-height:17px;color:var(--muted)}
.tutor .links{position:relative;margin-top:12px;display:flex;justify-content:center;gap:8px}
.tutor .links i{display:block;width:14px;height:14px;border-radius:2px;background:var(--blue)}
.tutor .links i:last-child{background:#d9453a}
.footer{left:0;top:2452px;width:1200px;height:238px;background:var(--blue);color:#fff}
.footer h5{font-size:17px;font-weight:500;margin-bottom:16px}
.footer p{font-size:12px;line-height:20px}
.col{top:46px}
.footer input{margin-top:16px;width:215px;height:30px;border:0;padding-left:10px;font-size:12px;background:#eee}
.footer .sub{display:inline-block;margin-top:12px;padding:8px 15px;background:var(--black);font-size:12px;border-radius:3px}
.follow{display:flex;align-items:center;gap:16px;margin-bottom:12px;font-size:12px}
.follow i{display:block;width:32px;height:32px;border-radius:50%;border:1px solid #fff}
.bottom{left:0;top:2690px;width:1200px;height:105px;background:var(--black);color:#fff;font-size:12px;text-align:center;line-height:82px}
</style>
</head>
<body>
<header class="topbar">
  <div class="contact">
    <span><svg width="13" height="13" viewBox="0 0 24 24"><path fill="#fff" d="M6.6 10.8a15 15 0 0 0 6.6 6.6l2.2-2.2a1 1 0 0 1 1-.25 11 11 0 0 0 3.6.6 1 1 0 0 1 1 1V20a1 1 0 0 1-1 1A17 17 0 0 1 3 4a1 1 0 0 1 1-1h3.5a1 1 0 0 1 1 1c0 1.25.2 2.45.6 3.6a1 1 0 0 1-.25 1z"/></svg>555-210-4477</span>
    <span><svg width="14" height="11" viewBox="0 0 24 18"><path fill="#fff" d="M0 0h24v18H0z"/><path fill="none" stroke="#1a72c0" stroke-width="2" d="M1 1l11 8 11-8"/></svg>hello@samplemail.net</span>
  </div>
  <div class="lang">ENGLISH ▾</div>
  <div class="social"><i></i><i></i><i></i><i></i><i></i></div>
</header>

<nav class="nav">
  <div class="logo"><i></i>K5Lesson</div>
  <div class="menu">
    <a class="active">HOME</a><a>ABOUT US</a><a>TUTORS</a><a>COURSES</a><a>PRICING</a><a>CAREERS</a><a>CONTACT US</a>
  </div>
</nav>

<section class="hero" role="img" aria-label="Photo of a student and a tutor studying together at a desk in a library">
  <h1>K5LESSON.COM PROVIDES</h1>
  <p>QUALITY ONLINE TUTORING TO ITS USERS IN KUWAIT</p>
  <div class="arrow" style="left:1028px"><svg width="38" height="38"><path d="M22 12l-7 7 7 7" stroke="#fff" stroke-width="2.5" fill="none"/></svg></div>
  <div class="arrow" style="left:1073px"><svg width="38" height="38"><path d="M16 12l7 7-7 7" stroke="#fff" stroke-width="2.5" fill="none"/></svg></div>
</section>

<section class="welcome">
  <h2>WELCOME TO <b>K5LESSON</b></h2>
  <p>K5Lesson.com provides quality online tutoring to its users in Kuwait with ease, and at a very affordable price. Online tutoring through K5Lesson.com offers prompt academic support to its users who get connected to tutors instantly when they are ready to learn. Besides online tutoring K5Lesson.com also provides test prep, homework prep, supplemental tutoring and expert assistance before tests and exams. Our online tutoring services are customized for students from Grades 1- 12 .</p>
</section>

<section class="steps">
  <div class="step" style="left:81px">
    <div class="dot" style="background:var(--orange)"><svg width="40" height="36" viewBox="0 0 40 36"><rect x="2" y="2" width="36" height="24" rx="2" fill="#fff"/><rect x="16" y="26" width="8" height="5" fill="#fff"/><rect x="11" y="31" width="18" height="3" fill="#fff"/></svg></div>
    <h3>STEP 1</h3><p>CREATE AN ACCOUNT</p>
  </div>
  <div class="step" style="left:439px">
    <div class="dot" style="background:var(--green)"><svg width="36" height="40" viewBox="0 0 36 40"><path d="M8 2h24l-6 36H2z" fill="#fff"/><path d="M11 10h16M10 16h15M9 22h14" stroke="#8cc63f" stroke-width="2"/></svg></div>
    <h3>STEP 2</h3><p>CHOOSE YOUR PLAN</p>
  </div>
  <div class="step" style="left:804px">
    <div class="dot" style="background:var(--sky)"><svg width="44" height="32" viewBox="0 0 44 32"><rect x="7" y="2" width="30" height="20" rx="2" fill="none" stroke="#fff" stroke-width="3"/><path d="M2 26h40l-3 4H5z" fill="#fff"/></svg></div>
    <h3>STEP 3</h3><p>CONNECT TO YOUR ONLINE<br>CLASSROOM</p>
  </div>
</section>

<section class="about">
  <div class="photo" role="img" aria-label="Photo of a tutor helping a young boy with homework at a table"></div>
  <h2>KNOW MORE <b>ABOUT K5LESSON</b></h2>
  <p style="top:114px">We have highly talented, experienced and professional teachers, who are just a click away and available to address any type of academic query that students might have. Our online tutors have many years of experience tutoring in their subjects for grades K-12 and beyond.</p>
  <p style="top:196px;height:96px;overflow:hidden">Our customized programs are designed to help students understand the basic and give them practical knowledge to understand the subject in a better way, so they may perform exceptionally well in the exams. Our tutors are given rigorous training for the specific curriculum standards required across grades. We believe that all students are not alike. All our tutoring</p>
  <div class="btn-green">Read More</div>
</section>

<section class="courses" role="img" aria-label="Dark photo of hands typing on a laptop keyboard">
  <h2>COURSES OFFERED</h2>
  <p>Lorem Ipsum has been the industry's standard dummy text ever since the 1500s, when an unknown printer took a galley of type and scrambled it to make a type specimen book. It has survived not only five centuries, but also the leap into electronic</p>
  <div class="btn-ghost">READ MORE</div>
</section>

<section class="tutors">
  <h2>OUR <b>TUTORS</b></h2>
  <div class="tutor" style="left:95px"><div class="face" role="img" aria-label="Portrait photo of a tutor"></div><h4>Neque porro quisquam</h4><p>Lorem Ipsum has been the industry's standard dummy text ever since the 1500s, when an unknown printer took</p><div class="links"><i></i><i></i><i></i><i></i></div></div>
  <div class="tutor" style="left:352px"><div class="face" role="img" aria-label="Portrait photo of a tutor"></div><h4>Neque porro quisquam</h4><p>Lorem Ipsum has been the industry's standard dummy text ever since the 1500s, when an unknown printer took</p><div class="links"><i></i><i></i><i></i><i></i></div></div>
  <div class="tutor" style="left:609px"><div class="face" role="img" aria-label="Portrait photo of a tutor"></div><h4>Neque porro quisquam</h4><p>Lorem Ipsum has been the industry's standard dummy text ever since the 1500s, when an unknown printer took</p><div class="links"><i></i><i></i><i></i><i></i></div></div>
  <div class="tutor" style="left:866px"><div class="face" role="img" aria-label="Portrait photo of a tutor"></div><h4>Neque porro quisquam</h4><p>Lorem Ipsum has been the industry's standard dummy text ever since the 1500s, when an unknown printer took</p><div class="links"><i></i><i></i><i></i><i></i></div></div>
</section>

<footer class="footer">
  <div class="col" style="left:101px;width:240px">
    <h5>NEWSLETTERS SIGN UP</h5>
    <p>Sign up for our daily email by entering your information below</p>
    <input type="text" placeholder="Email address"><br>
    <span class="sub">SUBSCRIBE</span>
  </div>
  <div class="col" style="left:391px;width:240px">
    <h5>K5LESSON</h5>
    <p>Lorem Ipsum has been the industry's standard dummy text ever since the 1500s, when an unknown printer took</p>
    <p style="margin-top:10px">a galley of type and scrambled it to make a type specimen book. It has survived not</p>
  </div>
  <div class="col" style="left:710px;width:240px">
    <h5>GET IN TOUCH</h5>
    <p>Address : 14 Harlow Lane, Eastgate</p>
    <p style="margin-top:10px">Fenwick, FN4 2RD</p>
    <p style="margin-top:18px">Phone : 555-210-4477</p>
    <p style="margin-top:18px">Email : hello@samplemail.net</p>
  </div>
  <div class="col" style="left:974px;width:200px">
    <h5>FOLLOW US ON</h5>
    <div class="follow" style="position:relative"><i></i>Friendly</div>
    <div class="follow" style="position:relative"><i></i>Chirper</div>
    <div class="follow" style="position:relative"><i></i>Snapgram</div>
  </div>
</footer>

<div class="bottom">Copyright © 2016. All Rights Reserved</div>
</body>
</html>
```